New Template design for Website in Wordpress

We are interested in changing our website look at www.haulvantix.com -We also are very interested in Have it done in Wordpress in which we are understanding the search engines are liking a bit more. The website we would want to try working with on this is www.haulvantix.com. We look forward to seeing the different design ideas please just make sure they are in wordpress! Thanks, Merrick

Reason: need more design idea..... We would still like to use our pictures off our site since we paid for them so keep that in mind as well as we would still want the rotating pictures in the head of the page but not in Flash.

```html
<!DOCTYPE html>
<html lang="en">
<head>
<meta charset="utf-8">
<title>Haulvantix – A Diversified Freight Company</title>
<link href="https://fonts.googleapis.com/css2?family=Ubuntu:wght@400;500;700&family=Montserrat:wght@400;600&family=Open+Sans:wght@400;600&display=swap" rel="stylesheet">
<style>
:root{
  --brand-red:#8f1309;
  --card-red:#9a1207;
  --dark:#252525;
  --text-grey:#8a8a8a;
  --heading-grey:#5a5a5a;
  --nav-grey:#4a4a4a;
  --footer:#343434;
  --page:#ffffff;
  --read-more-yellow:#f5e15a;
}
*{margin:0;padding:0;box-sizing:border-box}
html,body{width:1166px;height:1200px;overflow:hidden;background:var(--page)}
body{position:relative;font-family:"Open Sans",Arial,sans-serif;color:var(--text-grey)}

.top-rule{position:absolute;left:0;top:0;width:1166px;height:5px;background:#b9b9b9}
.site-header{position:absolute;left:0;top:5px;width:1166px;height:120px;background:linear-gradient(#ffffff,#f4f4f4);box-shadow:0 2px 4px rgba(0,0,0,.12);z-index:2}
.brand-name{position:absolute;left:106px;top:30px;font-family:"Ubuntu",sans-serif;font-weight:700;font-size:32px;letter-spacing:1px;color:var(--brand-red)}
.brand-tagline{position:absolute;left:107px;top:72px;font-family:"Open Sans",sans-serif;font-size:17px;color:#6b6b6b;letter-spacing:.2px}
.social-ribbons{position:absolute;left:916px;top:0;display:flex;gap:10px}
.social-ribbons svg{display:block}
.main-nav{position:absolute;left:489px;top:62px;display:flex;align-items:center;font-family:"Ubuntu",sans-serif;font-size:14px;color:var(--nav-grey)}
.main-nav a{color:inherit;text-decoration:none;padding:6px 12px;margin-right:2px}
.main-nav a.active{background:var(--brand-red);color:#fff}
.main-nav .call{color:var(--brand-red);font-weight:500;font-size:16px;margin-left:4px}

.hero{position:absolute;left:0;top:125px;width:1166px;height:543px}
.hero-photo{position:absolute;inset:0;background:linear-gradient(90deg,#e8e6e9 0%,#e4e2e6 45%,#a6adba 100%)}
.hero-title{position:absolute;left:107px;top:126px;font-family:"Montserrat",sans-serif;font-weight:400;font-size:27px;line-height:37px;color:#555;text-transform:uppercase}
.hero-title strong{color:var(--brand-red);font-weight:600}
.hero-title .sub{color:var(--brand-red)}
.hero-text{position:absolute;left:107px;width:400px;font-size:13.5px;line-height:20px;color:#777}
.hero-text.one{top:212px}
.hero-text.two{top:265px}
.hero-button{position:absolute;left:107px;top:310px;width:215px;height:45px;background:var(--dark);color:#fff;border-radius:3px;font-family:"Ubuntu",sans-serif;font-size:17px;line-height:45px;text-align:center}
.slide-dots{position:absolute;left:107px;top:372px;display:flex;gap:3px}
.slide-dots span{width:22px;height:3px;background:#c9c9c9}
.slide-dots span.on{background:var(--brand-red)}

.services{position:absolute;left:107px;top:577px;width:953px;height:331px;background:#fff;padding:9px 9px 0}
.service-row{display:flex}
.service{width:234px;height:322px}
.service-photo{height:158px}
.service-body{height:164px;padding-top:16px;text-align:center;color:#fff}
.service.dark .service-body{background:var(--dark)}
.service.red .service-body{background:var(--card-red)}
.service h3{font-family:"Ubuntu",sans-serif;font-weight:500;font-size:16px;line-height:22px;text-transform:uppercase;letter-spacing:.2px}
.service p{margin:9px auto 0;width:210px;font-size:11px;line-height:17.5px;color:#e2e2e2}
.service.red p{color:#f0d6d3}
.service .more{display:block;margin-top:8px;font-size:10.5px;color:var(--read-more-yellow)}

.info-col{position:absolute;top:922px}
.info-col.left{left:116px;width:450px}
.info-col.right{left:601px;width:448px}
.info-divider{position:absolute;left:583px;top:925px;width:1px;height:208px;background:#e4e4e4}
.info-col h2{font-family:"Montserrat",sans-serif;font-weight:400;font-size:18px;line-height:25px;color:var(--heading-grey);text-transform:uppercase;white-space:nowrap}
.info-col p{margin-top:8px;font-size:12.3px;line-height:19.5px;color:#8c8c8c}
.more-left{position:absolute;left:115px;top:1117px;font-size:11px;color:var(--brand-red)}
.more-right{position:absolute;left:600px;top:1117px;font-size:11px;color:var(--brand-red)}

.site-footer{position:absolute;left:0;top:1158px;width:1166px;height:42px;background:var(--footer);color:#a8a8a8;font-size:12.5px;line-height:42px;text-align:center}
</style>
</head>
<body>
<div class="top-rule"></div>
<header class="site-header">
  <div class="brand-name">HAULVANTIX</div>
  <div class="brand-tagline">A DIVERSIFIED FREIGHT COMPANY</div>
  <div class="social-ribbons" aria-label="Social links">
    <svg width="30" height="42" viewBox="0 0 30 42"><path d="M0 0H30V34L15 42L0 34Z" fill="#1fa8dc"/></svg>
    <svg width="30" height="42" viewBox="0 0 30 42"><path d="M0 0H30V34L15 42L0 34Z" fill="#3b5aa0"/></svg>
    <svg width="30" height="42" viewBox="0 0 30 42"><path d="M0 0H30V34L15 42L0 34Z" fill="#de4a37"/></svg>
    <svg width="30" height="42" viewBox="0 0 30 42"><path d="M0 0H30V34L15 42L0 34Z" fill="#2f8dc4"/></svg>
  </div>
  <nav class="main-nav">
    <a class="active" href="#">HOME</a>
    <a href="#">INSURANCE &amp; LEGAL INFO</a>
    <a href="#">FAST FREIGHT QUOTE</a>
    <span class="call">CALL: (888)555-0142</span>
  </nav>
</header>

<section class="hero">
  <div class="hero-photo" role="img" aria-label="Container ship loaded with stacked cargo containers at port cranes"></div>
  <h1 class="hero-title">Welcome to the <strong>Haulvantix</strong><br><span class="sub">(A Diversified Freight Company)</span></h1>
  <p class="hero-text one">Lorem ipsum dolor sit amet, consectetur adipisicing elit, sed do eiusmod tempor incididunt ut labore et dolore magna aliqua.</p>
  <p class="hero-text two">Ut enim ad minim veniam, quis nostrud exercitation ullamco laboris nisi ut aliquip ex ea commodo consequat..</p>
  <div class="hero-button">FREE FREIGHT QUOTE</div>
  <div class="slide-dots"><span class="on"></span><span></span><span></span><span></span></div>
</section>

<section class="services">
  <div class="service-row">
    <article class="service dark">
      <div class="service-photo" role="img" aria-label="Truck hauling an oversize load on a highway" style="background:linear-gradient(180deg,#9fb3c4,#7d7a63)"></div>
      <div class="service-body"><h3>Heavy Haul<br>Services</h3><p>Lorem ipsum dolor sit amet, consecte tur adipisicing elit, sed do eiusmod tempor incididunt magna aliqua.</p><span class="more">+ READ MORE</span></div>
    </article>
    <article class="service red">
      <div class="service-photo" role="img" aria-label="Red semi truck with refrigerated trailer" style="background:linear-gradient(180deg,#d6d8dc,#a8a4a6)"></div>
      <div class="service-body"><h3>Dry &amp; Refrigerated<br>Services</h3><p>Lorem ipsum dolor sit amet, consecte tur adipisicing elit, sed do eiusmod tempor incididunt magna aliqua.</p><span class="more">+ READ MORE</span></div>
    </article>
    <article class="service dark">
      <div class="service-photo" role="img" aria-label="Flatbed truck driving on an open road" style="background:linear-gradient(180deg,#96978f,#aeafa9)"></div>
      <div class="service-body"><h3>Flatbed, Step Deck<br>&amp; Piggy Back Services</h3><p>Lorem ipsum dolor sit amet, consecte tur adipisicing elit, sed do eiusmod tempor incididunt magna aliqua.</p><span class="more">+ READ MORE</span></div>
    </article>
    <article class="service red">
      <div class="service-photo" role="img" aria-label="Cargo ship sailing on the open ocean" style="background:linear-gradient(180deg,#cfd9e2,#5f7689)"></div>
      <div class="service-body"><h3>Freight Forwarding<br>Ocean Services</h3><p>Lorem ipsum dolor sit amet, consecte tur adipisicing elit, sed do eiusmod tempor incididunt magna aliqua.</p><span class="more">+ READ MORE</span></div>
    </article>
  </div>
</section>

<section class="info-col left">
  <h2>Worldwide Shipping- Ocean and Trucking<br>with No Limits</h2>
  <p>Welcome to Haulvantix and Meridian Cargo Inc. We are a one stop solution logistics company servicing Worldwide with our Trucking and Ocean shipping service. In using our freight services, we will negotiate a competitive freight quote using over 5000 different carriers who are certified and contracted by us. We have all equipment types available daily, service all freight types, and have no limits Worldwide.</p>
</section>
<div class="info-divider"></div>
<section class="info-col right">
  <h2>Get Fast &amp; Free Freight Quotes Now<br>and Save!!</h2>
  <p>Lorem ipsum dolor sit amet, consectetur adipiscing elit, sed do eiusmod tempor incididunt ut labore et dolore magna aliqua. Ut enim ad minim veniam, quis nostrud exercitation ullamco laboris nisi ut aliquip ex ea commodo conse- quat. Duis aute irure dolor in reprehenderit in voluptate velit esse cillum dolore eu fugiat nulla pariatur. Excepteur sint occaecat cupidatat non proident, sunt in culpa qui officia deserunt mollit anim id est laborum.</p>
</section>
<a class="more-left">+ READ MORE</a>
<a class="more-right">+ READ MORE</a>

<footer class="site-footer">Copyrights ©2014 Haulvantix.com - All Rights reserved</footer>
</body>
</html>
```